Business card design for a world class martial arts and group fitness facility

We need a professional and eye catching design for a business card. The card will be used in networking as well as marketing.
We are a martial arts facility offering Taekwondo, Brazilian Jiu Jitsu, and group fitness. All of our programs are geared for kids and adults.
Our Taekwondo program is lead by a Hall of Fame instructor who was Instructor of the Year in 2015.
Our Brazilian Jiu Jitsu program is lead by a wold class instructor who is also a part of the renown Brazilian KVO team.
We offer 3 focused group fitness programs: Ring striking, Pulse Fitness, and The Meadow which are all lead by certified instructors in a small group setting.
Our facility is state of the art and has been recognized as such in nationally published magazines.
Our business is named The Lantern which is the linear logo that is attached. This is the main logo. I also attached a circular logo we have used in some marketing material. Our Jiu Jitsu program is the KVO team logo. The Taekwondo program is the TORVEX Prime. It would be nice to somehow incorporate all 3 logos, but The Lantern is most important.
Industry/Entity Type
Martial Art
Contact Information for Business Card
We would like to use all 3 logos if possible but The Lantern is the most important. We would like to have a place for a staff member's name while keeping the focus on the programs we offer.
Look and feel
Each slider illustrates characteristics of the customer's brand and the style your logo design should communicate.

```html
<!DOCTYPE html>
<html lang="en">
<head>
<meta charset="utf-8">
<title>The Lantern – Business Card</title>
<link rel="stylesheet" href="https://fonts.googleapis.com/css2?family=Questrial&display=swap">
<style>
  :root {
    --page: #ebe6de;
    --card-light: #ffffff;
    --card-dark: #0e0e0e;
    --ink: #1c1c1c;
    --rust: #b8472a;
    --rust-soft: #a9442a;
    --white: #f4f4f4;
  }
  * { box-sizing: border-box; margin: 0; padding: 0; }
  html, body {
    width: 734px; height: 1200px; overflow: hidden;
    background: var(--page);
    font-family: "Questrial", "Century Gothic", sans-serif;
  }
  .canvas { position: relative; width: 734px; height: 1200px; }

  .card {
    position: absolute; left: 57px;
    width: 620px; height: 354px;
    border-radius: 18px;
    overflow: hidden;
    box-shadow: 0 10px 28px rgba(0,0,0,.18);
  }
  .card--front { top: 150px; background: var(--card-light); color: var(--ink); }
  .card--back  { top: 696px; background: var(--card-dark); color: var(--white); }

  /* front */
  .brand-mark {
    position: absolute; left: 48px; top: 108px;
    display: flex; align-items: center; gap: 14px;
  }
  .brand-mark__dot { width: 22px; height: 22px; background: var(--rust); }
  .brand-mark__name { font-size: 52px; letter-spacing: 1px; color: var(--ink); white-space: nowrap; }
  .staff { position: absolute; left: 330px; top: 196px; }
  .staff__name { font-size: 30px; letter-spacing: .5px; }
  .staff__title { font-size: 13px; color: var(--rust); letter-spacing: 1px; margin-top: 4px; }
  .contact {
    position: absolute; left: 48px; right: 40px; bottom: 34px;
    display: flex; justify-content: space-between;
    font-size: 14px; color: var(--ink);
  }
  .contact__item { display: flex; align-items: center; gap: 7px; }
  .contact__item svg { width: 13px; height: 13px; fill: var(--rust); }

  /* back */
  .emblem {
    position: absolute; right: 48px; top: 72px;
    display: flex; align-items: center; gap: 14px;
  }
  .emblem__dot { width: 22px; height: 22px; border-radius: 50%; background: var(--rust-soft); }
  .emblem__name { font-size: 44px; color: var(--rust-soft); white-space: nowrap; }

  .program-list {
    position: absolute; left: 40px; right: 40px; bottom: 36px;
    display: flex; align-items: flex-end; gap: 60px;
  }
  .program { display: flex; flex-direction: column; gap: 10px; }
  .program__mark { display: flex; align-items: center; gap: 12px; height: 64px; }
  .program__badge {
    width: 58px; height: 58px; border-radius: 50%;
    border: 3px solid var(--rust); background: var(--white);
  }
  .program__name { font-size: 26px; color: var(--white); white-space: nowrap; }
  .program__label {
    display: flex; align-items: center; gap: 7px;
    font-size: 15px; color: var(--white); white-space: nowrap;
  }
  .program__label svg { width: 13px; height: 13px; stroke: var(--rust); fill: none; stroke-width: 3; }
</style>
</head>
<body>
<main class="canvas">

  <section class="card card--front" aria-label="Card front">
    <div class="brand-mark">
      <span class="brand-mark__dot"></span>
      <span class="brand-mark__name">The Lantern</span>
    </div>
    <div class="staff">
      <p class="staff__name">Your Name</p>
      <p class="staff__title">JOB TITLE</p>
    </div>
    <div class="contact">
      <span class="contact__item">
        <svg viewBox="0 0 16 16"><path d="M3 1h3l1.5 4-2 1.3a9 9 0 0 0 4.2 4.2L11 8.5l4 1.5v3a2 2 0 0 1-2 2A13 13 0 0 1 1 3a2 2 0 0 1 2-2z"/></svg>
        000 000 0000
      </span>
      <span class="contact__item">
        <svg viewBox="0 0 16 16"><path d="M1 3h14v10H1z M1 3l7 6 7-6" stroke="#fff" stroke-width="1"/></svg>
        Email@xyz.com
      </span>
      <span class="contact__item">
        <svg viewBox="0 0 16 16"><circle cx="8" cy="8" r="7"/><path d="M1 8h14M8 1c-3 4-3 10 0 14M8 1c3 4 3 10 0 14" stroke="#fff" stroke-width="1" fill="none"/></svg>
        www.website.com
      </span>
    </div>
  </section>

  <section class="card card--back" aria-label="Card back">
    <div class="emblem">
      <span class="emblem__dot"></span>
      <span class="emblem__name">The Lantern</span>
    </div>
    <div class="program-list">
      <div class="program">
        <div class="program__mark">
          <span class="program__name">TORVEX Prime</span>
        </div>
        <p class="program__label">
          <svg viewBox="0 0 16 16"><path d="M2 8l4 4 8-9"/></svg>
          The Taekwondo
        </p>
      </div>
      <div class="program">
        <div class="program__mark">
          <span class="program__badge"></span>
          <span class="program__name">KVO</span>
        </div>
        <p class="program__label">
          <svg viewBox="0 0 16 16"><path d="M2 8l4 4 8-9"/></svg>
          Jiu Jitsu program
        </p>
      </div>
    </div>
  </section>

</main>
</body>
</html>
```